Brand Identity Redesign for Harbourline Painting - DELIVERABLE - Brand Guide Poster

DELIVERABLE - Brand Guide Poster (see attached Brand Guide Poster 1 and Brand Guide example 2).
- We are seeking graphic designers who can help us reimagine and revamp our brand identity based on our new Harbourline Painting logo. We are looking for a fresh and modern approach that aligns with our values and attracts our target audience.
- The task involves creating a comprehensive brand identity system that includes:
- Logo variations and usage guidelines
- Colour palette selection and guidelines
- Typography selection and guidelines
- Graphic elements, patterns, or textures
- Visual style guidelines for various applications (e.g., website, social media, marketing materials - online and offline)
- Brand collateral design (business cards, letterheads, brochures, quotes, invoices, proposals, vehicle signage, yard signage, worksite signage, etc.)
- The designer should have experience in brand identity design and a strong portfolio showcasing their skills in creating visually appealing and cohesive brand identities.
- The project will require collaboration, as we will provide our new logo and any specific design preferences, and expect the designer to incorporate these elements while offering their creative expertise.
- The deliverables should be provided in digital formats (e.g., vector files, design software files) and accompanied by a brand guidelines document explaining the proper usage of the brand identity elements. See attached example of brand guidelines poster. A one page guide like this would be awesome.

Target Market(s)

1. Wealthy Home Owners with a primary residence and holiday homes on the Central Coast of NSW Overview: Harbourline Painting works extensively with wealthy home owners on the Central Coast of NSW who own beachside properties. These customers typically require extensive maintenance and protection from corrosion due to the harsh coastal environment. 2. Companies who manage multiple properties in New South Wales.

Industry/Entity Type

Painting and decorating

Font styles to use
Serif
Sans Serif

Requirements
Must have
• Overall style should exude sophistication, professionalism, and attention to detail. The design should convey a sense of craftsmanship and longevity, emphasizing the company's focus on protecting surfaces for long-lasting durability. The logo should be sleek, clean, and modern, while still maintaining a classic and timeless feel. It should be versatile and scalable to ensure it can be used across various marketing materials. Brand guidelines poster - see attached example.
Should not have
• Very bright colours that look cheap. I have attached some logos that will be displayed on all our marketing along with a colour scheme that complements them and the logo. I am, however, very open to suggestions.

```html
<!DOCTYPE html>
<html lang="en">
<head>
<meta charset="utf-8">
<title>Harbourline Painting — Brand Guidelines</title>
<link href="https://fonts.googleapis.com/css2?family=Cinzel:wght@400;600&family=Poppins:ital,wght@0,400;0,600;1,400&display=swap" rel="stylesheet">
<style>
  :root{
    --navy:#354652; --slate:#5F7077; --mist:#91A3A7; --rust:#905336;
    --sage:#777A65; --taupe:#B39A86; --blush:#E8D5C7; --cloud:#EDEDED;
    --ink:#333333; --ash:#A1A1A1; --paper:#FEFEFE; --grey:#8a8a8a;
    --serif:'Cinzel', 'Times New Roman', serif;
    --sans:'Poppins', Arial, sans-serif;
  }
  *{box-sizing:border-box;margin:0;padding:0}
  html,body{width:897px;height:1200px;overflow:hidden;background:#fff}
  .poster{position:absolute;left:111px;top:122px;width:670px;height:957px;background:var(--paper);box-shadow:0 12px 40px rgba(0,0,0,.28)}
  .abs{position:absolute}

  /* header */
  .hero{left:8px;top:8px;width:303px;height:128px;background:var(--navy)}
  .hero-title{left:53px;top:30px;font-family:var(--serif);color:#fff;font-size:39px;line-height:40px;letter-spacing:1px}
  .stripes{left:311px;top:8px;display:flex;height:128px}
  .stripes span{width:16px;height:100%}
  .hero-bar{left:8px;top:136px;width:654px;height:12px;background:var(--rust)}

  /* wordmark */
  .wordmark{font-family:var(--serif);font-weight:400;text-align:center;line-height:1;white-space:nowrap}
  .wordmark .name{display:block}
  .wordmark .sub{display:block;letter-spacing:.4em;margin-top:.3em}
  .wm-navy{color:var(--navy)} .wm-ink{color:var(--ink)} .wm-white{color:#fff} .wm-blush{color:var(--blush)}

  /* headings */
  .section-title{font-family:var(--serif);color:var(--rust);font-size:21px;line-height:23px;font-weight:400}
  .section-title.large{font-size:22px;line-height:24px}
  .rule{height:1.5px;background:var(--rust)}
  .vrule{width:1.5px;background:var(--rust)}
  .label{font-family:var(--sans);font-weight:600;font-size:6.4px;color:var(--ink);letter-spacing:.1px}
  .label.rust{color:var(--rust);text-align:center;line-height:9px}
  .copy{font-family:var(--sans);font-size:4.9px;line-height:7.2px;color:#444}
  .copy.italic{font-style:italic}

  .logo-box{background:#302a28;display:flex;align-items:center;justify-content:center}
  .clear-box{border:.6px solid #999;background:#fff}
  .marker{background:var(--navy)}

  /* palette */
  .swatch{left:169px;width:62px;height:14px;font-family:var(--sans);font-size:5px;line-height:14px;padding-left:4px;color:#fff}
  .swatch.light{color:#555;border:.5px solid #bbb}

  /* media */
  .card{box-shadow:0 2px 6px rgba(0,0,0,.25);overflow:hidden}
  .tiny{font-family:var(--sans);font-size:2.6px;line-height:3.6px;color:#666}
  .tiny.white{color:#ddd}

  /* typography band */
  .type-band{left:8px;top:893px;width:654px;height:57px;background:var(--sage)}
  .type-col{text-align:center;color:var(--blush)}
  .type-divider{width:1.5px;background:var(--blush)}
</style>
</head>
<body>
<main class="poster">

  <!-- header -->
  <div class="abs hero"></div>
  <h1 class="abs hero-title">BRAND<br>GUIDELINES</h1>
  <div class="abs stripes">
    <span style="background:var(--cloud)"></span><span style="background:var(--blush)"></span>
    <span style="background:var(--taupe)"></span><span style="background:var(--sage)"></span>
    <span style="background:var(--rust)"></span><span style="background:var(--mist)"></span>
    <span style="background:var(--slate)"></span><span style="background:var(--navy)"></span>
  </div>
  <div class="abs hero-bar"></div>
  <div class="abs wordmark wm-navy" style="left:468px;top:55px;width:170px">
    <span class="name" style="font-size:18px">HARBOURLINE</span>
    <span class="sub" style="font-size:7px">PAINTING</span>
  </div>

  <!-- logo overview -->
  <h2 class="abs section-title" style="left:64px;top:165px">LOGO<br>OVERVIEW</h2>
  <div class="abs rule" style="left:143px;top:171px;width:193px"></div>
  <p class="abs copy italic" style="left:64px;top:219px;width:90px">The Harbourline Painting logo communicates the brand's nature of business while also symbolizing the brand's story.</p>
  <p class="abs copy italic" style="left:197px;top:219px;width:93px">The rules about how to use the logo are meant to make sure that it is used the same way every time. This can help the logo gain value and recognition over time.</p>

  <!-- size and proportion -->
  <p class="abs label" style="left:365px;top:206px">SIZE AND PROPORTION</p>
  <p class="abs copy" style="left:365px;top:220px;width:165px">The logo treatment to the right is one of several secondary logo treatments for Harbourline Painting.</p>
  <div class="abs wordmark wm-navy" style="left:572px;top:218px;width:48px">
    <span class="name" style="font-size:5.2px">HARBOURLINE</span>
    <span class="sub" style="font-size:2.6px">PAINTING</span>
  </div>
  <svg class="abs" style="left:572px;top:203px" width="62" height="42" viewBox="0 0 62 42" aria-hidden="true">
    <g stroke="#2b7bbf" stroke-width=".6" fill="#2b7bbf">
      <line x1="57" y1="0" x2="57" y2="41"/>
      <polygon points="55,10 59,10 57,13" stroke="none"/>
      <polygon points="55,30 59,30 57,27" stroke="none"/>
      <line x1="2" y1="30" x2="42" y2="30"/>
      <polygon points="2,28 2,32 0,30" stroke="none"/>
      <polygon points="42,28 42,32 44,30" stroke="none"/>
    </g>
    <rect x="46" y="16" width="13" height="6" fill="#fff"/>
    <text x="52.5" y="21" font-family="Poppins, sans-serif" font-size="4" fill="#2b7bbf" text-anchor="middle">0.22"</text>
    <text x="22" y="29" font-family="Poppins, sans-serif" font-size="3.4" fill="#2b7bbf" text-anchor="middle">1"</text>
  </svg>

  <div class="abs vrule" style="left:335px;top:262px;height:301px"></div>

  <!-- logo variation -->
  <h2 class="abs section-title large" style="left:66px;top:272px">LOGO<br>VARIATION</h2>
  <p class="abs label" style="left:67px;top:327px">PRIMARY LOGO</p>
  <div class="abs wordmark wm-navy" style="left:64px;top:348px;width:104px">
    <span class="name" style="font-size:11.5px">HARBOURLINE</span>
    <span class="sub" style="font-size:5px">PAINTING</span>
  </div>
  <p class="abs label" style="left:197px;top:327px">SECONDARY LOGO</p>
  <div class="abs logo-box" style="left:199px;top:338px;width:115px;height:42px">
    <div class="wordmark wm-blush"><span class="name" style="font-size:11.5px">HARBOURLINE</span><span class="sub" style="font-size:5px">PAINTING</span></div>
  </div>
  <p class="abs label" style="left:67px;top:387px">BLACK LOGO</p>
  <div class="abs wordmark wm-ink" style="left:64px;top:407px;width:104px">
    <span class="name" style="font-size:11.5px">HARBOURLINE</span>
    <span class="sub" style="font-size:5px">PAINTING</span>
  </div>
  <p class="abs label" style="left:197px;top:387px">WHITE LOGO</p>
  <div class="abs logo-box" style="left:199px;top:398px;width:115px;height:42px">
    <div class="wordmark wm-white"><span class="name" style="font-size:11.5px">HARBOURLINE</span><span class="sub" style="font-size:5px">PAINTING</span></div>
  </div>

  <!-- clear space -->
  <p class="abs label" style="left:64px;top:458px">CLEAR SPACE REQUIREMENTS</p>
  <p class="abs copy italic" style="left:64px;top:471px;width:250px">To ensure the impact and integrity of the mark, a certain amount of white space is required around the logo on all sides. A space of 'I' (marked in the example provided), which is measured from the height</p>
  <div class="abs clear-box" style="left:65px;top:502px;width:167px;height:61px"></div>
  <div class="abs marker" style="left:65px;top:519px;width:16px;height:14px"></div>
  <div class="abs marker" style="left:216px;top:502px;width:16px;height:14px"></div>
  <div class="abs marker" style="left:65px;top:549px;width:16px;height:14px"></div>
  <div class="abs wordmark wm-navy" style="left:83px;top:520px;width:130px">
    <span class="name" style="font-size:14px">HARBOURLINE</span>
    <span class="sub" style="font-size:6px">PAINTING</span>
  </div>

  <!-- unacceptable -->
  <h2 class="abs section-title" style="left:366px;top:260px;font-size:22px;line-height:24px">UNACCEPTABLE LOGO<br>TREATMENTS</h2>

  <p class="abs label rust" style="left:358px;top:322px;width:100px">DO NOT REARRANGE</p>
  <div class="abs wordmark wm-navy" style="left:368px;top:344px;width:80px"><span class="name" style="font-size:8px">HARBOURLINE</span><span class="sub" style="font-size:3.6px">PAINTING</span></div>

  <p class="abs label rust" style="left:530px;top:322px;width:100px">DO NOT DISTORT</p>
  <div class="abs wordmark wm-navy" style="left:540px;top:344px;width:80px"><span class="name" style="font-size:8px">HARBOURLINE</span><span class="sub" style="font-size:3.6px">PAINTING</span></div>

  <p class="abs label rust" style="left:358px;top:374px;width:100px">DO NOT ADD A STROKE</p>
  <div class="abs wordmark wm-navy" style="left:368px;top:395px;width:80px"><span class="name" style="font-size:8px">HARBOURLINE</span><span class="sub" style="font-size:3.6px">PAINTING</span></div>

  <p class="abs label rust" style="left:515px;top:378px;width:130px">DO NOT ADD A DROP SHADOW</p>
  <div class="abs wordmark wm-navy" style="left:540px;top:400px;width:80px"><span class="name" style="font-size:8px">HARBOURLINE</span><span class="sub" style="font-size:3.6px">PAINTING</span></div>

  <p class="abs label rust" style="left:358px;top:424px;width:100px">DO NOT ALTER SPACING</p>
  <div class="abs wordmark wm-navy" style="left:368px;top:446px;width:80px"><span class="name" style="font-size:8px">HARBOURLINE</span><span class="sub" style="font-size:3.6px">PAINTING</span></div>

  <p class="abs label rust" style="left:515px;top:424px;width:130px">DO NOT USE WORD MARK<br>WITHOUT THE COMPLETE LOGO</p>
  <div class="abs wordmark wm-navy" style="left:540px;top:450px;width:80px"><span class="name" style="font-size:8px">HARBOURLINE</span></div>

  <p class="abs label rust" style="left:358px;top:472px;width:100px">DO NOT CHANGE<br>THE TYPEFACE</p>
  <div class="abs wordmark wm-navy" style="left:368px;top:495px;width:80px"><span class="name" style="font-size:8px">HARBOURLINE</span><span class="sub" style="font-size:3.6px">PAINTING</span></div>

  <p class="abs label rust" style="left:515px;top:472px;width:130px">DO NOT CHANGE THE COLOR</p>
  <div class="abs wordmark wm-navy" style="left:540px;top:495px;width:80px"><span class="name" style="font-size:8px">HARBOURLINE</span><span class="sub" style="font-size:3.6px">PAINTING</span></div>

  <p class="abs label rust" style="left:424px;top:525px;width:130px">DO NOT PLACE A JPEG ON A<br>COLOR BACKGROUND</p>
  <div class="abs" style="left:365px;top:544px;width:266px;height:20px;background:var(--navy)"></div>
  <div class="abs" style="left:455px;top:545px;width:68px;height:18px;background:#fff"></div>
  <div class="abs wordmark wm-navy" style="left:455px;top:548px;width:68px"><span class="name" style="font-size:7px">HARBOURLINE</span><span class="sub" style="font-size:3.2px">PAINTING</span></div>

  <!-- divider band -->
  <div class="abs" style="left:8px;top:591px;width:654px;height:3px;background:var(--taupe)"></div>
  <div class="abs" style="left:8px;top:594px;width:654px;height:6px;background:var(--slate)"></div>

  <!-- color palette -->
  <h2 class="abs section-title" style="left:64px;top:620px;font-size:21px;color:var(--taupe)">COLOR PALETTE</h2>
  <p class="abs label" style="left:64px;top:648px;font-size:6.6px">Core colors</p>
  <p class="abs copy italic" style="left:64px;top:664px;width:100px">Use these color proportions in any layout or collateral design. Text should always be set in black, navy blue and white.</p>
  <p class="abs copy italic" style="left:64px;top:700px;width:95px">Green and red can be used as accent colors in the proportions shown above.</p>
  <p class="abs copy italic" style="left:64px;top:762px;color:#777">Note:</p>
  <p class="abs copy italic" style="left:64px;top:775px;width:82px;line-height:6.3px;color:#777">Use Pantone values for offset printing or for a vendor to reference for optimal color output. Use RGB values for digital outputs. Use HEX values for web outputs. Use CMYK values for printed outputs.</p>

  <div class="abs swatch" style="top:649px;background:var(--navy)">HEX#354652</div>
  <div class="abs swatch" style="top:669px;background:var(--slate)">HEX #5F7077</div>
  <div class="abs swatch" style="top:690px;background:var(--mist)">HEX #91A3A7</div>
  <div class="abs swatch" style="top:710px;background:var(--rust)">HEX #905336</div>
  <div class="abs swatch" style="top:731px;background:var(--sage)">HEX #777A65</div>
  <div class="abs swatch" style="top:751px;background:var(--taupe)">HEX #B39A86</div>
  <div class="abs swatch light" style="top:771px;background:var(--blush)">HEX #E8D5C7</div>
  <div class="abs swatch light" style="top:792px;background:var(--cloud)">HEX #EDEDED</div>
  <div class="abs swatch" style="top:812px;background:var(--ink)">HEX #333333</div>
  <div class="abs swatch" style="top:833px;background:var(--ash)">HEX #A1A1A1</div>
  <div class="abs swatch light" style="top:853px;background:var(--paper)">HEX #FEFEFE</div>

  <div class="abs vrule" style="left:335px;top:624px;height:242px"></div>

  <!-- media applied -->
  <h2 class="abs section-title" style="left:366px;top:620px;font-size:21px;color:var(--navy)">MEDIA APPLIED</h2>

  <!-- business card front -->
  <div class="abs card" style="left:371px;top:681px;width:106px;height:62px;background:#1f2a33">
    <div class="abs" style="left:0;top:0;width:37px;height:62px;background:#fff"></div>
    <div class="abs" style="left:37px;top:0;width:3px;height:62px;background:var(--ink)"></div>
    <div class="abs" style="left:40px;top:0;width:3px;height:62px;background:var(--slate)"></div>
    <div class="abs" style="left:43px;top:0;width:3px;height:62px;background:var(--rust)"></div>
    <div class="abs wordmark wm-navy" style="left:-8px;top:26px;width:50px;transform:rotate(-90deg)"><span class="name" style="font-size:5px">HARBOURLINE</span><span class="sub" style="font-size:2.4px">PAINTING</span></div>
    <p class="abs" style="left:52px;top:13px;font-family:var(--sans);font-weight:600;font-size:3.6px;color:#fff">JHON DOE</p>
    <p class="abs tiny white" style="left:52px;top:18px">CEO</p>
    <svg class="abs" style="left:52px;top:25px" width="4" height="30" viewBox="0 0 4 30" aria-hidden="true" fill="#ddd">
      <circle cx="2" cy="2" r="1.4"/>
      <rect x=".4" y="8.5" width="3.2" height="2.2"/>
      <path d="M.6 15.5 l1 0 l.6 1 l-.5 .6 l1.2 1.2 l.6 -.5 l1 .6 l0 1 q-3 .2 -3.9 -3.9z"/>
      <circle cx="2" cy="24" r="1.5" fill="none" stroke="#ddd" stroke-width=".4"/>
    </svg>
    <p class="abs tiny white" style="left:58px;top:25px">12 Shore Rd, Gosford</p>
    <p class="abs tiny white" style="left:58px;top:32px">hello@harbourlinepainting.com</p>
    <p class="abs tiny white" style="left:58px;top:39px">123-456-7890</p>
    <p class="abs tiny white" style="left:58px;top:47px">www.harbourlinepainting.com</p>
  </div>

  <!-- business card back -->
  <div class="abs card" style="left:370px;top:769px;width:106px;height:73px">
    <div style="height:10px;background:var(--navy)"></div>
    <div style="height:10px;background:var(--mist)"></div>
    <div style="height:33px;background:#fff;display:flex;align-items:center;justify-content:center">
      <div class="wordmark wm-navy"><span class="name" style="font-size:7px">HARBOURLINE</span><span class="sub" style="font-size:3px">PAINTING</span></div>
    </div>
    <div style="height:10px;background:var(--taupe)"></div>
    <div style="height:10px;background:var(--rust)"></div>
  </div>

  <!-- letterhead -->
  <div class="abs card" style="left:499px;top:671px;width:133px;height:189px;background:#fff">
    <div class="abs" style="left:0;top:0;width:6px;height:189px;background:var(--rust)"></div>
    <div class="abs wordmark wm-navy" style="left:14px;top:14px;width:50px"><span class="name" style="font-size:6.5px">HARBOURLINE</span><span class="sub" style="font-size:2.8px">PAINTING</span></div>
    <div class="abs" style="left:74px;top:13px;width:59px;height:15px;background:var(--sage)"></div>
    <p class="abs tiny white" style="left:74px;top:15px;width:56px;text-align:right;font-size:2.2px;line-height:3px">123-456-7890<br>hello@harbourlinepainting.com<br>12 Shore Rd, Gosford</p>
    <p class="abs tiny" style="left:14px;top:43px">To:<br>Marta Ellison<br>12 Shore Rd,<br>Gosford NSW 2250</p>
    <p class="abs tiny" style="left:96px;top:47px">October 20, 2025</p>
    <p class="abs tiny" style="left:14px;top:70px">Greetings!</p>
    <p class="abs tiny" style="left:14px;top:81px;width:106px">Thank you for choosing us for your coastal home. Our team protects every surface with premium coatings built to resist salt, sun and wind, so your finish stays fresh for years to come.</p>
    <p class="abs tiny" style="left:14px;top:100px;width:106px">We will visit the site to confirm colours, prepare a detailed quote and schedule works at a time that suits you and your family.</p>
    <p class="abs tiny" style="left:88px;top:129px">Regards,</p>
    <div class="abs" role="img" aria-label="Handwritten signature" style="left:78px;top:136px;width:38px;height:7px;background:linear-gradient(90deg,rgba(160,160,160,.15),rgba(160,160,160,.35),rgba(160,160,160,.15))"></div>
    <p class="abs tiny" style="left:88px;top:148px;text-align:center">Jhon Doe<br>CEO</p>
    <p class="abs tiny" style="left:14px;top:176px;font-size:2.2px">www.harbourlinepainting.com</p>
    <div class="abs" style="left:80px;top:176px;width:53px;height:5px;background:var(--blush)"></div>
  </div>

  <!-- typography -->
  <div class="abs type-band"></div>
  <div class="abs type-col" style="left:14px;top:901px;width:44px">
    <div style="font-family:var(--serif);font-size:19px;line-height:20px">AA</div>
    <div style="font-family:var(--serif);font-size:6px">TRAJAN</div>
  </div>
  <div class="abs type-col" style="left:62px;top:900px;width:110px;font-family:var(--serif);font-size:6.8px;line-height:9.6px">
    PRIMARY<br>ABCDEFGHIKLMOPQRZ<br>ABCDFEGHIJKLM<br>0123456789
  </div>
  <div class="abs type-divider" style="left:226px;top:901px;height:41px"></div>
  <div class="abs type-col" style="left:230px;top:908px;width:210px;font-family:var(--serif);font-size:20px;line-height:24px">TYPOGRAPHY</div>
  <div class="abs type-divider" style="left:443px;top:901px;height:41px"></div>
  <div class="abs type-col" style="left:500px;top:900px;width:112px;font-family:var(--sans);font-size:6.6px;line-height:10px">
    <span style="font-weight:600">SECONDARY</span><br>ABCDFEGHIJKLM<br>abcdefghiklmopqrz<br>0123456789
  </div>
  <div class="abs type-col" style="left:615px;top:900px;width:42px;font-family:var(--sans)">
    <div style="font-size:17px;line-height:20px">Aa</div>
    <div style="font-size:6px">POPPINS</div>
  </div>

</main>
</body>
</html>
```